Brightwell Wiring Needs A Logo Design

We need a logo for my new company based out of Sacramento, Ca called Brightwell Wiring. The name says it all, my electrical contracting business provides "Brightwell Craftsman Work" I'm open to any colors that pop and customers to say Wow. I would love to print my cards on metal.

Contact Information for Business Card

The card needs to have as follows
Name of company: Brightwell Wiring
My Name: Marco Delvane
Phone # 916-555-0147
CL# 4873920
Email: brightwellwiring@mailtorva.com
and a slogan that represent "BRIGHTWELL"

Requirements
Must have
• The card needs to have as follows
• Name of company: Brightwell Wiring
• My Name : Marco Delvane
• Phone # 916-555-0147
• CL# 4873920
• Email: brightwellwiring@mailtorva.com
• and a slogan that represent "BRIGHTWELL"
Nice to have
• popping colors
• electrical Arcing

```html
<!DOCTYPE html>
<html lang="en">
<head>
<meta charset="utf-8">
<title>Brightwell Wiring – Business Card</title>
<link href="https://fonts.googleapis.com/css2?family=Montserrat:wght@400;700;800&display=swap" rel="stylesheet">
<style>
  :root {
    --page: #d9d4cc;
    --card: #0b0b0c;
    --card-sheen: #2a2a2d;
    --blue: #1f86c8;
    --orange: #f2a21f;
    --white: #ffffff;
    --text-soft: #e9e9ea;
  }
  * { margin: 0; padding: 0; box-sizing: border-box; }
  html, body {
    width: 1200px;
    height: 1022px;
    overflow: hidden;
    background: var(--page);
  }
  .business-card {
    position: absolute;
    left: 100px;
    top: 226px;
    width: 1000px;
    height: 570px;
    background: radial-gradient(ellipse 60% 70% at 38% 45%, var(--card-sheen) 0%, var(--card) 70%);
    overflow: hidden;
    font-family: "Montserrat", sans-serif;
    color: var(--white);
  }
  .brand-mark {
    position: absolute;
    left: 70px;
    top: 232px;
    display: flex;
    align-items: center;
    gap: 16px;
  }
  .brand-mark__square {
    width: 34px;
    height: 34px;
    background: var(--blue);
    flex: none;
  }
  .brand-mark__name {
    font-weight: 800;
    font-size: 42px;
    letter-spacing: 1px;
    text-transform: uppercase;
    white-space: nowrap;
    color: var(--orange);
  }
  .slogan {
    position: absolute;
    left: 70px;
    top: 300px;
    font-weight: 800;
    font-size: 25px;
    letter-spacing: 1.5px;
    text-transform: uppercase;
    white-space: nowrap;
  }
  .contact-list {
    position: absolute;
    left: 380px;
    top: 380px;
    list-style: none;
    font-weight: 400;
    font-size: 21px;
    line-height: 32px;
    color: var(--text-soft);
  }
  .contact-list__item {
    display: flex;
    align-items: center;
    gap: 14px;
  }
  .contact-list__icon {
    width: 16px;
    height: 16px;
    flex: none;
  }
  .name-tab {
    position: absolute;
    right: 0;
    top: 150px;
    width: 400px;
    height: 74px;
    background: var(--blue);
    clip-path: polygon(36px 0, 100% 0, 100% 100%, 0 100%);
    display: flex;
    align-items: center;
    padding-left: 58px;
    padding-right: 28px;
  }
  .name-tab__text {
    font-weight: 700;
    font-size: 31px;
    letter-spacing: 1px;
    text-transform: uppercase;
    white-space: nowrap;
  }
  .edge-stripe {
    position: absolute;
    left: 0;
    bottom: 0;
    width: 100%;
    height: 42px;
    display: flex;
  }
  .edge-stripe__blue { width: 53%; background: var(--blue); }
  .edge-stripe__orange { flex: 1; background: var(--orange); }
</style>
</head>
<body>
  <article class="business-card">
    <div class="brand-mark">
      <span class="brand-mark__square"></span>
      <span class="brand-mark__name">Brightwell Wiring</span>
    </div>
    <p class="slogan">Brightwell Craftsman Work</p>

    <div class="name-tab">
      <span class="name-tab__text">Marco Delvane</span>
    </div>

    <ul class="contact-list">
      <li class="contact-list__item">
        <svg class="contact-list__icon" viewBox="0 0 16 16" aria-hidden="true">
          <rect x="2" y="3" width="12" height="10" fill="none" stroke="#f2a21f" stroke-width="1.6"/>
        </svg>
        <span>4873920</span>
      </li>
      <li class="contact-list__item">
        <svg class="contact-list__icon" viewBox="0 0 16 16" aria-hidden="true">
          <path d="M4 2 L6.5 5 L5 6.8 Q6.5 9.8 9.2 11 L11 9.5 L14 12 L12.3 14 Q5 13 2 4 Z" fill="#f2a21f"/>
        </svg>
        <span>916-555-0147</span>
      </li>
      <li class="contact-list__item">
        <svg class="contact-list__icon" viewBox="0 0 16 16" aria-hidden="true">
          <rect x="1.5" y="3.5" width="13" height="9" fill="none" stroke="#f2a21f" stroke-width="1.6"/>
          <path d="M1.5 3.5 L8 9 L14.5 3.5" fill="none" stroke="#f2a21f" stroke-width="1.6"/>
        </svg>
        <span>brightwellwiring@mailtorva.com</span>
      </li>
    </ul>

    <div class="edge-stripe">
      <span class="edge-stripe__blue"></span>
      <span class="edge-stripe__orange"></span>
    </div>
  </article>
</body>
</html>
```